Brivo Australia Dental

I need to update my website and design. I have some ideas in mind and would like to replicate the format from another website into my own. I need the website to be easy to edit (I have no prior wordpress exp) after the design is complete. Please visit https://thewillowcradle.org.au/ for example of layout.
Target Market(s)
Parents and elder folks
Industry/Entity Type
Dental
Coding
Coded - Design and coding required
Number of Pages Required
4 page
Font styles to use
Sans Serif
Colors
0392cd
Requirements
Must have
- - Home, Services, About Us, News
- - Colours
- - Clear action from viewers
- - Location of business (able to change all the time)
- - Illustrations/ photos

```html
<!DOCTYPE html>
<html lang="en">
<head>
<meta charset="utf-8">
<title>Vellumi Australia Dental</title>
<link href="https://fonts.googleapis.com/css2?family=Poppins:wght@300;400;500;600&display=swap" rel="stylesheet">
<style>
:root{
  --blue:#0392cd;
  --blue-dark:#027bb0;
  --ink:#222;
  --text:#777;
  --muted:#999;
  --pale:#dff0fb;
  --pale-2:#c9e6f8;
  --grey:#f2f3f5;
  --line:#e6e6e6;
  --white:#fff;
}
*{box-sizing:border-box;margin:0;padding:0}
html,body{width:1200px;height:4816px;overflow:hidden}
body{position:relative;font-family:'Poppins',sans-serif;color:var(--text);background:var(--white);font-size:12px;line-height:1.6}
.abs{position:absolute}
.btn{position:absolute;display:flex;align-items:center;justify-content:center;background:var(--blue);color:var(--white);font-size:11px;font-weight:600;text-transform:uppercase;letter-spacing:.3px}
.ph{position:absolute}

/* top bar */
.topbar{left:0;top:0;width:1200px;height:41px;background:var(--blue);color:var(--white);font-size:11px}
.topbar .item{position:absolute;top:12px;display:flex;align-items:center;gap:6px}
.social{position:absolute;display:flex;gap:6px}
.social span{width:30px;height:30px;border-radius:50%;background:var(--white);display:block}
.social.blue span{background:var(--blue)}

/* header */
.header{left:0;top:41px;width:1200px;height:62px;background:var(--white)}
.brand{position:absolute;left:93px;top:9px;display:flex;align-items:center;gap:8px}
.brand .dot{width:14px;height:14px;border-radius:50%;background:var(--blue)}
.brand .name{font-size:26px;font-weight:400;color:var(--blue);line-height:1}
.brand .tag{position:absolute;left:0;top:36px;font-size:8px;color:var(--blue);white-space:nowrap}
.nav{position:absolute;right:93px;top:22px;display:flex;gap:52px;font-size:12px;color:var(--muted)}
.nav .on{color:var(--blue)}

/* hero */
.hero{left:0;top:103px;width:1200px;height:465px;background:linear-gradient(90deg,#f6f9fb 0%,#eef4f8 55%,#f7fafc 100%);overflow:hidden}
.hero .photo{left:0;top:0;width:600px;height:465px;background:linear-gradient(135deg,#e9e3da,#cdbba6 55%,#efeae3)}
.hero .sub{right:93px;top:146px;font-size:42px;font-weight:600;color:var(--blue);line-height:1}
.hero h1{position:absolute;right:93px;top:190px;font-size:76px;font-weight:400;color:var(--ink);line-height:1}
.dots{position:absolute;left:1062px;top:418px;display:flex;gap:10px}
.dots span{width:8px;height:8px;border-radius:50%;background:var(--blue)}
.dots span:first-child{box-shadow:0 0 0 3px #cfe8f6}

/* features */
.features{left:0;top:568px;width:1200px;height:320px;background:linear-gradient(90deg,var(--pale),#eaf5fc 50%,var(--pale))}
.feature{position:absolute;top:46px;width:230px;text-align:center}
.feature .ring{width:140px;height:140px;margin:0 auto;border-radius:50%;background:var(--white);display:flex;align-items:center;justify-content:center;box-shadow:0 0 0 8px rgba(255,255,255,.45)}
.feature .ring .in{width:112px;height:112px;border-radius:50%;border:2px solid var(--blue);display:flex;align-items:center;justify-content:center}
.feature h3{font-size:15px;font-weight:400;color:var(--ink);margin-top:10px}
.feature p{font-size:11px;line-height:1.45;color:var(--text)}

/* welcome */
.welcome-img{left:587px;top:968px;width:520px;height:458px;background:linear-gradient(160deg,#eef1f4,#d6dde3 60%,#b9c4cd)}
.card{position:absolute;background:var(--white);box-shadow:0 2px 14px rgba(0,0,0,.09)}
.welcome{left:93px;top:1034px;width:535px;height:330px;padding:58px 28px 0}
.welcome h2{font-size:28px;font-weight:400;color:var(--ink);line-height:1.2}
.welcome .lead{font-size:12px;color:var(--blue);margin-top:10px;line-height:1.6}
.welcome p{font-size:11px;margin-top:8px;line-height:1.75}
.badge{position:absolute;left:583px;top:1304px;width:68px;height:68px;border-radius:50%;background:var(--blue);border:4px solid var(--white);display:flex;align-items:center;justify-content:center;color:var(--white);font-size:13px;box-shadow:0 2px 8px rgba(0,0,0,.15)}

/* cta */
.cta{left:0;top:1506px;width:1200px;height:266px;background:var(--blue);text-align:center;color:var(--white)}
.cta h2{position:absolute;left:0;width:1200px;top:78px;font-size:31px;font-weight:400;line-height:1.2}
.cta .call{position:absolute;left:479px;top:168px;width:240px;height:34px;background:#1a1a1a;color:var(--white);font-size:12px;display:flex;align-items:center;justify-content:center;gap:8px;border-radius:2px}
.notch{left:580px;top:1770px;width:0;height:0;border-left:20px solid transparent;border-right:20px solid transparent;border-top:18px solid var(--blue)}

/* section heading */
.sec-title{position:absolute;left:0;width:1200px;text-align:center;font-size:29px;font-weight:400;color:var(--ink)}
.sec-desc{position:absolute;left:150px;width:900px;text-align:center;font-size:11px;line-height:1.75;color:var(--text)}

/* services */
.svc-img{position:absolute;width:498px;height:333px}
.svc{position:absolute;width:498px;height:333px;padding:60px 38px 0}
.svc h3{font-size:22px;font-weight:400;color:var(--ink)}
.svc .lead{font-size:11.5px;color:var(--ink);margin-top:6px}
.svc p{font-size:11px;margin-top:8px;line-height:1.75;color:var(--text)}
.svc .btn{position:static;display:inline-flex;width:106px;height:32px;margin-top:14px}
.svc-icon{position:absolute;width:84px;height:84px;border-radius:50%;background:var(--blue);border:5px solid var(--white);box-shadow:0 2px 10px rgba(0,0,0,.15);display:flex;align-items:center;justify-content:center}

/* callback */
.callback{left:0;top:3574px;width:1200px;height:269px;background:var(--blue);color:var(--white)}
.callback h2{position:absolute;left:93px;top:52px;font-size:31px;font-weight:400}
.callback p{position:absolute;left:93px;top:110px;width:420px;font-size:11px;line-height:1.75}
.field{position:absolute;height:32px;background:var(--white);color:var(--muted);font-size:10px;padding:8px 10px}
.submit{left:626px;top:168px;width:104px;height:32px;background:#111}

/* news */
.news{position:absolute;top:4037px;width:327px;height:303px;background:var(--white);box-shadow:0 2px 12px rgba(0,0,0,.08)}
.news .img{height:184px;border-bottom:3px solid var(--blue)}
.news .date{position:absolute;left:0;top:184px;width:40px;height:40px;background:var(--blue);color:var(--white);text-align:center;font-size:14px;line-height:1.1;padding-top:5px}
.news .date small{display:block;font-size:8px}
.news h4{position:absolute;left:56px;top:195px;font-size:13px;font-weight:500;color:var(--ink);white-space:nowrap}
.news .meta{position:absolute;left:72px;top:215px;font-size:9px;color:var(--muted);display:flex;gap:30px}
.news p{position:absolute;left:10px;right:14px;top:244px;font-size:11px;line-height:1.6}

/* footer */
.footer{left:0;top:4373px;width:1200px;height:443px;background:var(--grey)}
.contact-bar{left:374px;top:4422px;width:826px;height:56px;background:var(--blue);border-radius:28px 0 0 28px;color:var(--white);font-size:10px;line-height:1.35}
.contact-bar .c{position:absolute;top:12px;display:flex;gap:8px;align-items:center}
.plane{left:304px;top:4405px;width:50px;height:50px;border-radius:50%;background:var(--white);border:2px solid var(--blue);display:flex;align-items:center;justify-content:center}
.newsletter{left:93px;top:4467px;width:268px;height:262px;background:#e9eaec;padding:36px 18px 0}
.newsletter h4{font-size:15px;font-weight:400;color:var(--ink)}
.newsletter p{font-size:11px;margin-top:8px;line-height:1.7}
.newsletter .in{height:30px;background:var(--white);font-size:9px;padding:8px 12px;margin-top:8px;color:var(--muted)}
.newsletter .btn{position:relative;margin:12px auto 0;width:108px;height:32px}
.fcol{position:absolute;top:4515px}
.fcol h4{font-size:14px;font-weight:400;color:var(--ink);margin-bottom:12px}
.fcol p{font-size:10.5px;line-height:1.75}
.fcol .who{color:var(--blue);font-weight:500;font-size:11px}
.rn{display:flex;gap:12px;margin-bottom:36px;font-size:10.5px;line-height:1.7}
.rn .av{width:38px;height:38px;border-radius:50%;background:linear-gradient(135deg,#e6d7c9,#b89c86);flex:none;margin-top:14px}
.rn .d{color:var(--text);margin-top:4px}
.svc-list{list-style:none;font-size:10.5px;line-height:2}
.svc-list li::before{content:"›";margin:0 18px 0 6px;color:var(--muted)}
.copy{left:0;top:4778px;width:1200px;text-align:center;font-size:10.5px;color:var(--text)}
.copy span{color:var(--blue)}
</style>
</head>
<body>

<!-- top bar -->
<div class="abs topbar">
  <div class="item" style="left:88px">
    <svg width="14" height="14" viewBox="0 0 24 24" fill="none" stroke="#fff" stroke-width="2"><path d="M5 3h4l2 5-3 2a12 12 0 0 0 6 6l2-3 5 2v4a2 2 0 0 1-2 2A17 17 0 0 1 3 5a2 2 0 0 1 2-2z"/></svg>
    Call Us : +0400 316 228
  </div>
  <div class="item" style="left:334px">
    <svg width="14" height="14" viewBox="0 0 24 24" fill="none" stroke="#fff" stroke-width="2"><path d="M12 22s7-7 7-12a7 7 0 0 0-14 0c0 5 7 12 7 12z"/><circle cx="12" cy="10" r="2.5"/></svg>
    Location : Lorem ipsum dollar,Australia
  </div>
  <div class="social" style="left:1001px;top:5px" aria-label="Social links"><span></span><span></span><span></span></div>
</div>

<!-- header -->
<header class="abs header">
  <div class="brand"><span class="name">vellumi</span><span class="dot"></span><span class="tag">for a better smile</span></div>
  <nav class="nav"><span class="on">Home</span><span>About</span><span>Services</span><span>News</span><span>Contact us</span></nav>
</header>

<!-- hero -->
<section class="abs hero">
  <div class="ph photo" role="img" aria-label="Photo of a smiling elderly couple"></div>
  <div class="ph sub">Gentle and Affordable</div>
  <h1>Dental Care</h1>
  <div class="btn" style="left:997px;top:290px;width:104px;height:34px">Call us now</div>
  <div class="dots"><span></span><span></span><span></span></div>
</section>

<!-- features -->
<section class="abs features">
  <div class="feature" style="left:96px;top:44px">
    <div class="ring"><div class="in">
      <svg width="64" height="64" viewBox="0 0 64 64" fill="none" stroke="#0392cd" stroke-width="2.5"><circle cx="32" cy="32" r="26"/><path d="M32 14v18l12 8"/></svg>
    </div></div>
    <h3>Always Available</h3>
    <p>There are many variations of passages of Lorem Ipsum available, but the majority</p>
  </div>
  <div class="feature" style="left:356px;top:60px">
    <div class="ring"><div class="in">
      <svg width="64" height="64" viewBox="0 0 64 64" fill="none" stroke="#0392cd" stroke-width="2.5"><circle cx="32" cy="26" r="16"/><path d="M32 17l3 6 6 1-4.5 4 1 6-5.5-3-5.5 3 1-6L23 24l6-1z"/><path d="M22 38l-4 20 8-5 6 7M42 38l4 20-8-5-6 7"/></svg>
    </div></div>
    <h3>Qualified Dentists</h3>
    <p>There are many variations of passages of Lorem Ipsum available, but the majority</p>
  </div>
  <div class="feature" style="left:614px;top:60px">
    <div class="ring"><div class="in">
      <svg width="64" height="64" viewBox="0 0 64 64" fill="none" stroke="#0392cd" stroke-width="2.5"><rect x="10" y="20" width="44" height="28" rx="12"/><path d="M18 48v8M46 48v8M28 20v-6h8v6"/><circle cx="44" cy="30" r="1.5" fill="#0392cd"/></svg>
    </div></div>
    <h3>Fair Prices</h3>
    <p>There are many variations of passages of Lorem Ipsum available, but the majority</p>
  </div>
  <div class="feature" style="left:872px;top:60px">
    <div class="ring"><div class="in">
      <svg width="64" height="64" viewBox="0 0 64 64" fill="none" stroke="#0392cd" stroke-width="2.5"><path d="M36 8l5 10 11 2-8 8 2 11-10-5-10 5 2-11-8-8 11-2z"/><path d="M8 50h10l10 4h14l12-8M18 46l8-2h10"/></svg>
    </div></div>
    <h3>Best Offers</h3>
    <p>There are many variations of passages of Lorem Ipsum available, but the majority</p>
  </div>
</section>

<!-- welcome -->
<div class="ph welcome-img" role="img" aria-label="Photo of a dentist holding an X-ray"></div>
<section class="card welcome">
  <h2>Welcome to Vellumi Australia</h2>
  <div class="lead">If you are going to use a passage of Lorem Ipsum, you need to be sure there isn't anything embarrassing hidden</div>
  <p>There are many variations of passages of Lorem Ipsum available, but the majority have suffered alteration in some form, by injected humour, or randomised words which don't look even slightly believable generators on the Internet tend to repeat predefined chunks as necessary .</p>
  <div class="btn" style="left:37px;top:268px;width:106px;height:32px">About us</div>
</section>
<div class="badge">vellumi</div>

<!-- cta -->
<section class="abs cta">
  <h2>Invest in your smile as early as possible and<br>enjoy the rest of your life</h2>
  <div class="call">
    <svg width="14" height="14" viewBox="0 0 24 24" fill="none" stroke="#fff" stroke-width="2"><path d="M5 3h4l2 5-3 2a12 12 0 0 0 6 6l2-3 5 2v4a2 2 0 0 1-2 2A17 17 0 0 1 3 5a2 2 0 0 1 2-2z"/></svg>
    CALL US (+0400) 316 228
  </div>
</section>
<div class="abs notch"></div>

<!-- services -->
<h2 class="sec-title" style="top:1838px">Dental Care Services</h2>
<p class="sec-desc" style="top:1884px">long established fact that a reader will be distracted by the readable content of a page when looking at its layout. The point of using Lorem Ipsum is that it has a more-or-less normal distribution of letters,</p>

<div class="svc-img" style="left:93px;top:1962px;background:linear-gradient(135deg,#eef1f3,#cfd9e0)" role="img" aria-label="Photo of a dentist examining a patient"></div>
<div class="card svc" style="left:609px;top:1962px">
  <h3>Tooth Protection</h3>
  <div class="lead">Lorem Ipsum is therefore always free from repetition .</div>
  <p>There are many variations of passages of Lorem Ipsum available, but the majority have suffered alteration in some form, by injected humour, or randomised words which don't look even slightly believable generators on the Internet tend to repeat predefined chunks as necessary .</p>
  <div class="btn">Read more</div>
</div>
<div class="svc-icon" style="left:558px;top:2085px"><svg width="40" height="40" viewBox="0 0 40 40" fill="none" stroke="#fff" stroke-width="2"><path d="M4 14c6-4 26-4 32 0M4 26c6 4 26 4 32 0M10 14v12M16 13v14M22 13v14M28 13v14"/></svg></div>

<div class="card svc" style="left:93px;top:2347px">
  <h3>Dental Implants</h3>
  <div class="lead">Lorem Ipsum is therefore always free from repetition .</div>
  <p>There are many variations of passages of Lorem Ipsum available, but the majority have suffered alteration in some form, by injected humour or randomised words which don't look even slightly believable generators on the Internet tend to repeat predefined chunks as necessary .</p>
  <div class="btn">Read more</div>
</div>
<div class="svc-img" style="left:609px;top:2347px;background:linear-gradient(135deg,#e7c9c0,#f4ece8 50%,#c89c90)" role="img" aria-label="Close-up photo of teeth during treatment"></div>
<div class="svc-icon" style="left:558px;top:2472px"><svg width="40" height="40" viewBox="0 0 40 40" fill="none" stroke="#fff" stroke-width="2"><path d="M11 6c3-2 6 0 9 0s6-2 9 0c3 3 1 8-9 8S8 9 11 6zM14 18h12M15 23h10M16 28h8M18 33h4"/></svg></div>

<div class="svc-img" style="left:93px;top:2723px;background:linear-gradient(135deg,#f1e4da,#dcc5b6 55%,#f5efe9)" role="img" aria-label="Close-up photo of a smile with a dental mirror"></div>
<div class="card svc" style="left:609px;top:2723px">
  <h3>Tooth Whitening</h3>
  <div class="lead">Lorem Ipsum is therefore always free from repetition .</div>
  <p>There are many variations of passages of Lorem Ipsum available, but the majority have suffered alteration in some form, by injected humour, or randomised words which don't look even slightly believable generators on the Internet tend to repeat predefined chunks as necessary .</p>
  <div class="btn">Read more</div>
</div>
<div class="svc-icon" style="left:558px;top:2848px"><svg width="40" height="40" viewBox="0 0 40 40" fill="#fff"><path d="M12 8c-5 0-7 5-6 10 1 4 2 6 3 12 1 4 4 4 5 0l2-7c1-2 3-2 4 0l2 7c1 4 4 4 5 0 1-6 2-8 3-12 1-5-1-10-6-10-3 0-4 2-6 2s-3-2-6-2z"/></svg></div>

<div class="card svc" style="left:93px;top:3108px">
  <h3>Prevention</h3>
  <div class="lead">Lorem Ipsum is therefore always free from repetition .</div>
  <p>There are many variations of passages of Lorem Ipsum available, but the majority have suffered alteration in some form, by injected humour or randomised words which don't look even slightly believable generators on the Internet tend to repeat predefined chunks as necessary .</p>
  <div class="btn">Read more</div>
</div>
<div class="svc-img" style="left:609px;top:3108px;background:linear-gradient(135deg,#e4c7bb,#f1e6e0 50%,#d2a89a)" role="img" aria-label="Close-up photo of a smile with braces"></div>
<div class="svc-icon" style="left:558px;top:3233px"><svg width="40" height="40" viewBox="0 0 40 40" fill="none" stroke="#fff" stroke-width="2"><path d="M12 6c-5 0-7 5-6 10 1 4 2 7 3 13 1 4 4 4 5 0l2-7c1-2 3-2 4 0l2 7c1 4 4 4 5 0 1-6 2-9 3-13 1-5-1-10-6-10-3 0-4 2-6 2s-3-2-6-2z"/><path d="M7 16h26M14 13v6M20 13v6M26 13v6"/></svg></div>

<div class="btn" style="left:547px;top:3463px;width:106px;height:32px">View all</div>

<!-- request a call back -->
<section class="abs callback">
  <h2>Request A call Back</h2>
  <p>There are many variations of passages of Lorem Ipsum available, but the majority have suffered alteration in some form, by injected humour, or randomised words which don't look even slightly believable generators on the Internet tend to repeat predefined chunks as necessary .</p>
  <div class="field" style="left:626px;top:74px;width:236px">Name :</div>
  <div class="field" style="left:873px;top:74px;width:234px">Email :</div>
  <div class="field" style="left:626px;top:118px;width:236px">Phone No :</div>
  <div class="field" style="left:873px;top:118px;width:234px;display:flex;justify-content:space-between">I want to know about<span>▾</span></div>
  <div class="btn submit">Submit now</div>
</section>

<!-- latest news -->
<h2 class="sec-title" style="top:3916px">Latest News</h2>
<p class="sec-desc" style="top:3962px">long established fact that a reader will be distracted by the readable content of a page when looking at its layout. The point of using Lorem Ipsum is that it has a more-or-less normal distribution of letters,</p>

<article class="news" style="left:93px">
  <div class="img" role="img" aria-label="Photo of a smiling senior couple" style="background:linear-gradient(135deg,#eef0f2,#cbc3ba)"></div>
  <div class="date">20<small>July</small></div>
  <h4>LOREM IPSUM IS NOT SIMPLY LAYOUT.</h4>
  <div class="meta"><span>by Admin</span><span>4 comments</span></div>
  <p>Many desktop publishing packages and web page editors now use Lorem Ipsum as their default model text,</p>
</article>
<article class="news" style="left:437px">
  <div class="img" role="img" aria-label="Photo of an elderly woman laughing" style="background:linear-gradient(135deg,#a9b08f,#d8d2c4 55%,#8f9a78)"></div>
  <div class="date">20<small>July</small></div>
  <h4>LOREM IPSUM IS NOT SIMPLY LAYOUT.</h4>
  <div class="meta"><span>by Admin</span><span>4 comments</span></div>
  <p>Many desktop publishing packages and web page editors now use Lorem Ipsum as their default model text,</p>
</article>
<article class="news" style="left:781px">
  <div class="img" role="img" aria-label="Photo of a grandmother with her family" style="background:linear-gradient(135deg,#f3efe9,#dcc7b3 55%,#f4f1ec)"></div>
  <div class="date">20<small>July</small></div>
  <h4>LOREM IPSUM IS NOT SIMPLY LAYOUT.</h4>
  <div class="meta"><span>by Admin</span><span>4 comments</span></div>
  <p>Many desktop publishing packages and web page editors now use Lorem Ipsum as their default model text,</p>
</article>

<!-- footer -->
<footer class="abs footer"></footer>
<div class="abs contact-bar">
  <div class="c" style="left:24px">
    <svg width="20" height="20" viewBox="0 0 24 24" fill="none" stroke="#fff" stroke-width="1.8"><path d="M5 3h4l2 5-3 2a12 12 0 0 0 6 6l2-3 5 2v4a2 2 0 0 1-2 2A17 17 0 0 1 3 5a2 2 0 0 1 2-2z"/></svg>
    <div>Phone :<br>+0400 316 228</div>
  </div>
  <div class="c" style="left:196px">
    <svg width="20" height="20" viewBox="0 0 24 24" fill="none" stroke="#fff" stroke-width="1.8"><path d="M12 22s7-7 7-12a7 7 0 0 0-14 0c0 5 7 12 7 12z"/><circle cx="12" cy="10" r="2.5"/></svg>
    <div>Location :<br>Lorem ipsum dollar</div>
  </div>
  <div class="c" style="left:386px">
    <svg width="20" height="20" viewBox="0 0 24 24" fill="none" stroke="#fff" stroke-width="1.8"><rect x="3" y="5" width="18" height="14" rx="1"/><path d="M3 6l9 7 9-7"/></svg>
    <div>Email :<br>hello@vellumidental.com.au</div>
  </div>
  <div class="c" style="left:596px">
    <svg width="20" height="20" viewBox="0 0 24 24" fill="none" stroke="#fff" stroke-width="1.8"><circle cx="12" cy="12" r="9"/><path d="M12 7v5l3 3"/></svg>
    <div>8am - 7pm<br>Monday to Saturday</div>
  </div>
</div>
<div class="abs plane"><svg width="24" height="24" viewBox="0 0 24 24" fill="#0392cd"><path d="M22 2L2 10l7 3 2 8 3-5 5 4z"/></svg></div>

<div class="abs newsletter">
  <h4>Newsletter</h4>
  <p>Many desktop publishing packages and web page editors now.</p>
  <div class="in">Your Name</div>
  <div class="in">Your Email</div>
  <div class="btn">Subscribe</div>
</div>

<div class="fcol" style="left:385px;width:250px">
  <h4>About Us</h4>
  <div class="who">Lena Ward , General Manager</div>
  <p>Publishing packages and web page editors now use Lorem Ipsum as their default model texto editors now use Lorem Ipsum as their default model text,</p>
  <div class="social blue" style="position:static;margin-top:16px" aria-label="Social links"><span></span><span></span><span></span></div>
</div>

<div class="fcol" style="left:690px;width:220px">
  <h4>Recent News</h4>
  <div class="rn"><div class="av" role="img" aria-label="Thumbnail photo"></div><div>Publishing packages and web page editors now<div class="d">▦ August 22,2019</div></div></div>
  <div class="rn"><div class="av" role="img" aria-label="Thumbnail photo"></div><div>Publishing packages and web page editors now<div class="d">▦ August 22,2019</div></div></div>
</div>

<div class="fcol" style="left:964px;width:150px">
  <h4>Our Services</h4>
  <ul class="svc-list">
    <li>Tooth Protection</li><li>Dental Implants</li><li>Teeth Whitening</li><li>Prevention</li><li>Oral surgery</li><li>Orthodontics</li><li>Root canal therapy</li><li>Dental Care</li>
  </ul>
</div>

<div class="abs copy">Copyright©2019 <span>vellumi</span> All Rights Reserved.</div>

</body>
</html>
```